Pelkey Realty LLC
Business Cards and Stationery
Modern
Dale Pelkey
Licensed Real Estate Broker ,Village Resident
4816 Marlow Crescent The Villages Florida 32158
dale58410@postlark.net
www.TopDeckFairwayParcels.com
When doing the web address make sure the T,D,F,and P are capital letters example www.TopDeckFairwayParcels.com also, The title should be licensed Real Estate Broker and UNDER that put Village Resident not beside of it.
dalepelkey dalepelkey
Great job alot of talent here Thank you all for the designs.sorry for ending contest early. Thank you so much
Both AI files have been uploaded one with the logo on top and one to the side. Just show me some nice modern business cards. Show me some in black n blue blue n white metallic etc. just make it look nice n modern. will check back monday to see the designs with feed back. Thanks

```html
<!DOCTYPE html>
<html lang="en">
<head>
<meta charset="utf-8">
<title>Pelkey Realty LLC – Business Cards</title>
<link rel="stylesheet" href="https://fonts.googleapis.com/css2?family=Cinzel:wght@500&family=Raleway:wght@300;400;500&display=swap">
<style>
  :root {
    --canvas: #e4e4e2;
    --card-black: #050608;
    --card-ink: #111318;
    --blue-deep: #0a2f7a;
    --blue-mid: #1553b8;
    --blue-bright: #2f7ce0;
    --blue-logo: #3d86e6;
    --silver: #c9ccd1;
    --white: #ffffff;
    --muted: #c8cdd6;
  }
  * { box-sizing: border-box; margin: 0; padding: 0; }
  html, body {
    width: 1200px; height: 901px; overflow: hidden;
    background: var(--canvas);
    font-family: "Raleway", sans-serif;
  }
  .stage {
    position: relative; width: 1200px; height: 901px;
  }
  .card {
    position: absolute; top: 296px;
    width: 540px; height: 309px;
    overflow: hidden;
    box-shadow: 0 6px 18px rgba(0,0,0,0.18);
  }
  /* Front */
  .card-front { left: 40px; background: var(--card-black); }
  .card-front .swoosh { position: absolute; inset: 0; width: 100%; height: 100%; }
  .brand {
    position: absolute; left: 30px; top: 34px;
    display: flex; align-items: center; gap: 12px;
  }
  .brand-square {
    width: 34px; height: 34px; border: 2px solid var(--blue-logo);
  }
  .brand-name {
    font-family: "Cinzel", serif; font-weight: 500;
    font-size: 25px; letter-spacing: 1.5px;
    color: var(--blue-logo); text-transform: uppercase;
  }
  .agent {
    position: absolute; left: 30px; top: 108px; color: var(--white);
  }
  .agent-name { font-size: 17px; font-weight: 400; margin-bottom: 4px; }
  .agent-role { font-size: 9.5px; font-weight: 300; line-height: 1.35; color: var(--muted); }
  .contact {
    position: absolute; right: 30px; top: 176px;
    width: 230px; color: var(--white);
    font-size: 11px; font-weight: 400; line-height: 1.4;
  }
  .contact-address { margin-bottom: 10px; }
  .contact-line { display: flex; align-items: center; gap: 5px; }
  .contact-line svg { width: 10px; height: 10px; fill: var(--white); flex: none; }
  .contact-web { margin-top: 6px; font-size: 11.5px; }
  /* Back */
  .card-back {
    left: 620px;
    background: linear-gradient(160deg, var(--blue-bright) 0%, var(--blue-mid) 45%, var(--blue-deep) 100%);
    display: flex; flex-direction: column; align-items: center; justify-content: center;
    color: var(--white);
  }
  .back-mark {
    width: 56px; height: 56px; border: 2px solid var(--white); margin-bottom: 16px;
  }
  .back-name {
    font-family: "Cinzel", serif; font-weight: 500;
    font-size: 24px; letter-spacing: 2px; text-transform: uppercase;
    margin-bottom: 14px;
  }
  .back-web { font-size: 12px; font-weight: 400; letter-spacing: 0.3px; }
</style>
</head>
<body>
<main class="stage">
  <section class="card card-front" aria-label="Business card front">
    <svg class="swoosh" viewBox="0 0 540 309" preserveAspectRatio="none" aria-hidden="true">
      <defs>
        <linearGradient id="silverBand" x1="0" y1="0" x2="1" y2="0">
          <stop offset="0" stop-color="#f4f5f7"/>
          <stop offset="0.5" stop-color="#9ea3ab"/>
          <stop offset="1" stop-color="#3a3d44"/>
        </linearGradient>
        <linearGradient id="blueBody" x1="0" y1="0" x2="0" y2="1">
          <stop offset="0" stop-color="#1a64cc"/>
          <stop offset="1" stop-color="#082a72"/>
        </linearGradient>
        <linearGradient id="blueGlow" x1="0" y1="0" x2="1" y2="0">
          <stop offset="0" stop-color="#0d3c96"/>
          <stop offset="1" stop-color="#3a8af0"/>
        </linearGradient>
      </defs>
      <rect width="540" height="309" fill="#050608"/>
      <path d="M0 198 C120 200 220 150 330 128 C420 110 480 112 540 104 L540 309 L0 309 Z" fill="url(#silverBand)"/>
      <path d="M0 214 C130 214 230 168 340 144 C430 126 490 124 540 120 L540 309 L0 309 Z" fill="#0b0d12"/>
      <path d="M0 232 C140 230 240 184 350 160 C440 142 495 140 540 138 L540 309 L0 309 Z" fill="url(#blueGlow)"/>
      <path d="M0 250 C150 246 250 200 360 178 C445 162 500 160 540 158 L540 309 L0 309 Z" fill="url(#blueBody)"/>
    </svg>

    <div class="brand">
      <span class="brand-square"></span>
      <span class="brand-name">Pelkey Realty LLC</span>
    </div>

    <div class="agent">
      <p class="agent-name">Dale Pelkey</p>
      <p class="agent-role">Licensed Real Estate Broker<br>Village Resident</p>
    </div>

    <div class="contact">
      <p class="contact-address">4816 Marlow Crescent The<br>Villages Florida 32158</p>
      <p class="contact-line">
        <svg viewBox="0 0 24 24"><path d="M6.6 10.8a15 15 0 0 0 6.6 6.6l2.2-2.2c.3-.3.7-.4 1-.2 1.1.4 2.3.6 3.6.6.6 0 1 .4 1 1V20c0 .6-.4 1-1 1C10.6 21 3 13.4 3 4c0-.6.4-1 1-1h3.5c.6 0 1 .4 1 1 0 1.3.2 2.5.6 3.6.1.3 0 .7-.2 1z"/></svg>
        407-555-0186
      </p>
      <p class="contact-line">
        <svg viewBox="0 0 24 24"><path d="M2 5h20v14H2z M3 6l9 7 9-7" fill="none" stroke="#fff" stroke-width="2"/></svg>
        dale58410@postlark.net
      </p>
      <p class="contact-web">www.TopDeckFairwayParcels.com</p>
    </div>
  </section>

  <section class="card card-back" aria-label="Business card back">
    <span class="back-mark"></span>
    <p class="back-name">Pelkey Realty LLC</p>
    <p class="back-web">www.TopDeckFairwayParcels.com</p>
  </section>
</main>
</body>
</html>
```